Brava-Lux.ch is looking for business card letterhead and envelope C5 with WOW effect

We need a strong business card for our company Brava-Lux.ch, logo is available. You want a black or dark background on which the logo Stark r% 26 # 252; appears. Letterhead and envelope in C5 format should be in a similar design, but does not have to be We need a strong business card for our company Brava-Lux.ch, logo is available. A black or dark background is desired, on which the logo Stark comes across. The letterhead and the envelope in C5 format should have a similar design.

Target Market(s)

Private customers as well as entrepreneurs

Contact Information for Business Card

E-mail: info@brava-lux.ch
Web.www.Brava-Lux.ch
Tel: +41 ( 0 ) 79 384 6027
Adresse:
Kellerweg 14
9405 Ostheim

Hier kann man Icons verwenden für Email,Tel und Adressse

Font styles to use
Other font styles liked:
• Dubai,bold

Colors

Designer to choose colors to be used in the design.

Requirements
Must have
• WOW effect
Nice to have
• R% 26 # 252; back business card with our service listings. - VEHICLE LABELING - SHOP WINDOW LABELING - STICKERS AND MUCH MORE ... in red color

```html
<!DOCTYPE html>
<html lang="en">
<head>
<meta charset="utf-8">
<title>Brava-Lux.ch Business Card</title>
<link rel="stylesheet" href="https://fonts.googleapis.com/css2?family=Montserrat:wght@600;700;800&family=Open+Sans:wght@400;600&display=swap">
<style>
  :root {
    --backdrop: #4a4239;
    --card: #1b1b1c;
    --card-edge: #232324;
    --white: #ffffff;
    --yellow: #fcc419;
    --red: #e0202a;
    --muted: #e6e6e6;
  }
  * { margin: 0; padding: 0; box-sizing: border-box; }
  html, body { width: 1200px; height: 930px; overflow: hidden; }
  body {
    background: var(--backdrop);
    font-family: "Open Sans", sans-serif;
    color: var(--white);
    position: relative;
  }
  .card {
    position: absolute;
    width: 580px;
    height: 375px;
    border-radius: 22px;
    background: linear-gradient(120deg, var(--card-edge) 0%, var(--card) 55%, #151516 100%);
    box-shadow: 0 14px 30px rgba(0,0,0,.45);
    overflow: hidden;
  }
  .card--front { left: 160px; top: 55px; }
  .card--back  { left: 460px; top: 495px; }

  .wordmark {
    display: flex;
    align-items: center;
    gap: 12px;
    font-family: "Montserrat", sans-serif;
    font-weight: 800;
    letter-spacing: 1px;
    color: var(--white);
    text-transform: uppercase;
  }
  .wordmark__square {
    width: 18px; height: 18px;
    background: var(--yellow);
    flex: none;
  }

  /* Front */
  .card--front .wordmark {
    position: absolute;
    right: 70px; top: 120px;
    font-size: 42px;
  }
  .services {
    position: absolute;
    right: 56px; top: 192px;
    list-style: none;
    text-align: right;
    font-size: 15px;
    line-height: 22px;
    text-transform: uppercase;
    letter-spacing: .3px;
  }
  .services li { display: flex; justify-content: flex-end; align-items: center; gap: 10px; }
  .services li::after {
    content: "";
    width: 8px; height: 8px;
    border: 2px solid var(--red);
    border-radius: 50%;
  }

  /* Back */
  .card--back .wordmark {
    position: absolute;
    left: 40px; top: 42px;
    font-size: 34px;
  }
  .person {
    position: absolute;
    left: 0; top: 178px;
    padding-left: 46px;
    border-left: 9px solid var(--yellow);
    margin-left: 34px;
  }
  .person__name {
    font-family: "Montserrat", sans-serif;
    font-weight: 700;
    font-size: 25px;
    letter-spacing: 1.5px;
    text-transform: uppercase;
    line-height: 1.1;
  }
  .person__surname { color: var(--yellow); }
  .person__role { font-size: 15px; margin-top: 4px; }
  .divider {
    position: absolute;
    left: 88px; top: 250px;
    width: 450px; height: 1px;
    background: var(--yellow);
  }
  .contacts {
    position: absolute;
    left: 88px; top: 268px;
    list-style: none;
    font-size: 15px;
    line-height: 26px;
    color: var(--muted);
  }
  .contacts li, .address { display: flex; align-items: center; gap: 10px; }
  .icon { width: 14px; height: 14px; flex: none; }
  .address {
    position: absolute;
    left: 350px; top: 268px;
    align-items: flex-start;
    font-size: 15px;
    line-height: 22px;
    color: var(--muted);
  }
  .address .icon { margin-top: 4px; width: 16px; height: 18px; }
</style>
</head>
<body>

  <section class="card card--front" aria-label="Business card front">
    <div class="wordmark"><span class="wordmark__square"></span>Brava-Lux.ch</div>
    <ul class="services">
      <li>Vehicle labeling</li>
      <li>Shop window labeling</li>
      <li>Stickers and much more</li>
    </ul>
  </section>

  <section class="card card--back" aria-label="Business card back">
    <div class="wordmark"><span class="wordmark__square"></span>Brava-Lux.ch</div>

    <div class="person">
      <p class="person__name">Lukas <span class="person__surname">Brenner</span></p>
      <p class="person__role">Director</p>
    </div>

    <div class="divider"></div>

    <ul class="contacts">
      <li>
        <svg class="icon" viewBox="0 0 24 24"><path fill="#fcc419" d="M6.6 10.8a15.1 15.1 0 0 0 6.6 6.6l2.2-2.2c.3-.3.7-.4 1-.2 1.1.4 2.3.6 3.6.6.6 0 1 .4 1 1V20c0 .6-.4 1-1 1A17 17 0 0 1 3 4c0-.6.4-1 1-1h3.5c.6 0 1 .4 1 1 0 1.3.2 2.5.6 3.6.1.3 0 .7-.2 1z"/></svg>
        +41 ( 0 ) 79 384 6027
      </li>
      <li>
        <svg class="icon" viewBox="0 0 24 24"><rect x="2.5" y="5" width="19" height="14" rx="1" fill="none" stroke="#fcc419" stroke-width="2"/><path d="M3 6l9 7 9-7" fill="none" stroke="#fcc419" stroke-width="2"/></svg>
        info@brava-lux.ch
      </li>
      <li>
        <svg class="icon" viewBox="0 0 24 24"><circle cx="12" cy="12" r="9.5" fill="none" stroke="#fcc419" stroke-width="2"/><path d="M2.5 12h19M12 2.5c3 3 3 16 0 19M12 2.5c-3 3-3 16 0 19" fill="none" stroke="#fcc419" stroke-width="1.6"/></svg>
        www.Brava-Lux.ch
      </li>
    </ul>

    <div class="address">
      <svg class="icon" viewBox="0 0 24 28"><path fill="#fcc419" d="M12 1a9 9 0 0 0-9 9c0 6.5 9 17 9 17s9-10.5 9-17a9 9 0 0 0-9-9zm0 12.5a3.5 3.5 0 1 1 0-7 3.5 3.5 0 0 1 0 7z"/></svg>
      <p>Kellerweg 14<br>9405 Ostheim</p>
    </div>
  </section>

</body>
</html>
```